Cake Bakery needs Large New Vibrant Window Decals

Our cake bakery is moving to a new location. We want to place window decals (vinyl) on 7 separate windows that are all the same size. (Image is attached for your reference. The windows are the ones within the red outline.)

The windows are approximately 76 inches tall and 98 inches wide. We have uploaded an image of the storefront to show you the 7 windows that need be to covered.

There are also 2 side by side doors that need a decals too. We have uploaded a logo we are using. You are allowed to change the logo color to better coordinate with a design you can create.

We want the colors to be bright and cheerful. You can see our current bakery website at brindlewoodsweets.example. ( I included the sign above our bakery if that helps you.)

Do not use any images of cakes or other bakery products in your design.

The graphics can be simple and clean or can be vivid and loud. We will consider all concepts.

You can create one design to be duplicated for each window or create a design that would flow across all the windows in a landscape effect.

Target Market(s)

People who purchase cakes for any occasion.

Industry/Entity Type

Bakery

Requirements
Must have
• Must have the logo on each window
Nice to have
• Open to any concepts
Should not have
• No images of cakes or other bakery products. The graphics must stand the test of time for the next 10 years.

```html
<!DOCTYPE html>
<html lang="en">
<head>
<meta charset="utf-8">
<title>Brindlewood Sweets — Window Decals</title>
<link href="https://fonts.googleapis.com/css2?family=Fredoka:wght@600&display=swap" rel="stylesheet">
<style>
  :root {
    --sheet: #e6e6e6;
    --white: #ffffff;
    --teal: #23cfa5;
    --pink: #f9a19e;
    --coral: #f37b7b;
    --purple: #5b3384;
    --lavender: #9f8cc3;
  }
  html, body {
    margin: 0;
    padding: 0;
    width: 909px;
    height: 1200px;
    overflow: hidden;
    background: var(--sheet);
  }
  .sheet {
    position: relative;
    width: 909px;
    height: 1200px;
    background: var(--sheet);
    font-family: "Fredoka", "Arial Rounded MT Bold", sans-serif;
  }
  .panel {
    position: absolute;
    overflow: hidden;
  }
  .panel svg {
    position: absolute;
    inset: 0;
    display: block;
  }
  .sign-board { left: 74px; top: 40px; width: 761px; height: 170px; background: var(--white); }
  .door-decal { left: 74px; top: 238px; width: 173px; height: 429px; }
  .window-decal { left: 288px; top: 240px; width: 547px; height: 424px; }

  .shop-name {
    position: absolute;
    margin: 0;
    color: var(--coral);
    font-weight: 600;
    text-align: center;
    line-height: 0.95;
    letter-spacing: -0.5px;
    white-space: nowrap;
  }
  .sign-board .shop-name {
    left: 0; right: 0; top: 66px;
    font-size: 29px;
  }
  .door-decal .shop-name {
    left: 0; right: 0; top: 88px;
    font-size: 24px;
  }
  .window-decal .name-plate {
    position: absolute;
    left: 128px; top: 150px;
    width: 290px; height: 110px;
    border-radius: 55px;
    background: var(--white);
  }
  .window-decal .shop-name {
    left: 128px; width: 290px; top: 166px;
    font-size: 40px;
  }
</style>
</head>
<body>
<main class="sheet">

  <section class="panel sign-board" aria-label="Storefront sign">
    <svg width="761" height="170" viewBox="0 0 761 170">
      <g class="stripes-left">
        <rect x="0" y="55" width="227" height="14" fill="var(--pink)"/>
        <rect x="0" y="69" width="227" height="14" fill="var(--teal)"/>
        <rect x="0" y="83" width="227" height="14" fill="var(--lavender)"/>
      </g>
      <g class="stripes-right">
        <rect x="534" y="55" width="227" height="14" fill="var(--pink)"/>
        <rect x="534" y="69" width="227" height="14" fill="var(--teal)"/>
        <rect x="534" y="83" width="227" height="14" fill="var(--lavender)"/>
      </g>
    </svg>
    <p class="shop-name">Brindlewood Sweets</p>
  </section>

  <section class="panel door-decal" aria-label="Door decal">
    <svg width="173" height="429" viewBox="0 0 173 429">
      <rect width="173" height="429" fill="var(--teal)"/>
      <path class="dome" d="M-4 212 Q86.5 168 177 212 V440 H-4 Z" fill="var(--pink)" stroke="var(--white)" stroke-width="3"/>
      <path class="scallops-top" d="M0 0 H173 V28 A28.8 18 0 0 1 115.3 28 A28.8 18 0 0 1 57.7 28 A28.8 18 0 0 1 0 28 Z" fill="var(--white)"/>
      <path class="clouds-bottom" d="M0 429 V400 A28.8 17 0 0 1 57.7 400 A28.8 17 0 0 1 115.3 400 A28.8 17 0 0 1 173 400 V429 Z" fill="var(--white)"/>
    </svg>
    <p class="shop-name">Brindlewood<br>Sweets</p>
  </section>

  <section class="panel window-decal" aria-label="Window decal">
    <svg width="547" height="424" viewBox="0 0 547 424">
      <rect width="547" height="424" fill="var(--teal)"/>
      <path class="dome" d="M60 345 C95 175 452 175 487 345 Z" fill="var(--pink)" stroke="var(--white)" stroke-width="4"/>
      <path class="scallops-top" d="M0 0 H547 V52 A54.7 36 0 0 1 437.6 52 A54.7 36 0 0 1 328.2 52 A54.7 36 0 0 1 218.8 52 A54.7 36 0 0 1 109.4 52 A54.7 36 0 0 1 0 52 Z" fill="var(--white)"/>
      <path class="clouds-bottom" d="M0 424 V372 A54.7 35 0 0 1 109.4 372 A54.7 35 0 0 1 218.8 372 A54.7 35 0 0 1 328.2 372 A54.7 35 0 0 1 437.6 372 A54.7 35 0 0 1 547 372 V424 Z" fill="var(--white)"/>
    </svg>
    <div class="name-plate"></div>
    <p class="shop-name">Brindlewood<br>Sweets</p>
  </section>

</main>
</body>
</html>
```